Vale Tinto - Compotas / new label of jams and honey.

Send the old one to know the text you should have.
height of compote bottle - one 8cm x6,5cm ather 5cmx4,5cm
cherry; Apple; Blackberry; fig; orange; wait; blueberry.
height honey jar 13cm
diameter 6,5cm
Updates

the logo may have another color

Target Market(s)

Expensive and different product ...
people with money

Colors

Designer to choose colors to be used in the design.

Requirements
Must have
• image of fruit
• three languages: Portuguese, French and English.
Nice to have
• black and more colors
• see our facebook
• https://www.facebook.com/valetintodoces/

```html
<!DOCTYPE html>
<html lang="en">
<head>
<meta charset="utf-8">
<title>Vale Tinto – Compotas label proposals</title>
<link rel="stylesheet" href="https://fonts.googleapis.com/css2?family=Arimo:ital,wght@0,400;0,700;1,400&family=Cormorant+Garamond:wght@500&family=Montserrat:wght@500&family=Oswald:wght@300;400&display=swap">
<style>
  :root {
    --ink: #000000;
    --paper: #ffffff;
    --note-red: #e8141b;
    --pumpkin: #f29021;
    --pumpkin-deep: #d9661a;
    --plum-dark: #4a1836;
    --plum-light: #8e3a67;
    --plum-flesh: #e8b64a;
    --muted: #d9d9d9;
  }
  * { box-sizing: border-box; margin: 0; padding: 0; }
  html, body { width: 1200px; height: 800px; overflow: hidden; background: var(--paper); }
  .board { position: relative; width: 1200px; height: 800px; }

  .note {
    position: absolute;
    color: var(--note-red);
    font-family: "Arimo", Arial, sans-serif;
    font-size: 27px;
    line-height: 34px;
    text-align: center;
    transform: translateX(-50%);
    white-space: nowrap;
    letter-spacing: 0.3px;
  }
  .note--additional { left: 198px; top: 79px; }
  .note--revised { left: 566px; top: 79px; }
  .note--approval { left: 962px; top: 131px; }

  /* ---------- Jar label ---------- */
  .label { position: absolute; top: 140px; width: 336px; height: 588px; color: var(--accent); }
  .label--pumpkin { left: 33px; --accent: var(--pumpkin); }
  .label--plum { left: 401px; --accent: var(--paper); }
  .label__shape { position: absolute; inset: 0; }

  .brand { position: absolute; left: 0; right: 0; top: 38px; text-align: center; }
  .brand__dot {
    display: block; width: 30px; height: 30px; margin: 0 auto 6px;
    border-radius: 50%; background: var(--muted);
  }
  .brand__name {
    font-family: "Cormorant Garamond", Georgia, serif;
    font-weight: 500; font-size: 14px; color: var(--muted); letter-spacing: 0.3px;
  }

  .fruit-art { position: absolute; border-radius: 50%; }
  .fruit-art--main { left: 117px; top: 114px; width: 94px; height: 98px; }
  .fruit-art--small { left: 137px; top: 386px; width: 56px; height: 64px; }
  .label--pumpkin .fruit-art {
    background: radial-gradient(circle at 50% 60%, var(--pumpkin) 0%, var(--pumpkin-deep) 55%, rgba(242,144,33,0.25) 72%, rgba(0,0,0,0) 74%);
  }
  .label--plum .fruit-art {
    background: radial-gradient(circle at 45% 55%, var(--plum-light) 0%, var(--plum-dark) 50%, var(--plum-flesh) 62%, rgba(255,255,255,0.2) 72%, rgba(0,0,0,0) 74%);
  }

  /* small nutrition panel on the stem */
  .mini-facts {
    position: absolute; left: 129px; top: 264px; width: 77px; height: 106px;
    border: 1px solid var(--accent); border-radius: 2px;
    padding: 3px 3px; font-family: "Arimo", Arial, sans-serif; color: var(--accent);
    font-size: 4.2px; line-height: 5.2px; white-space: nowrap; overflow: hidden;
  }
  .mini-facts__title { font-size: 6.2px; line-height: 8px; font-weight: 700; letter-spacing: -0.1px; }
  .mini-facts__sub { font-size: 3.5px; line-height: 4.2px; }
  .mini-facts__sub em { font-style: italic; }
  .mini-facts__bar { height: 2px; background: var(--accent); margin: 2px 0 1px; }
  .mini-facts__row { border-bottom: 0.6px solid var(--accent); padding: 1px 0 0.5px; }
  .mini-facts__row--plain { border-bottom: none; }
  .mini-facts__indent { padding-left: 4px; }
  .mini-facts__right { padding-left: 28px; }
  .mini-facts__note { font-size: 3.8px; margin-top: 3px; }

  .lettering {
    position: absolute; left: 81px; top: 474px; width: 166px; height: 42px;
    border-radius: 22px 6px 22px 6px;
    background: linear-gradient(90deg, rgba(0,0,0,0) 0%, var(--accent) 18%, var(--accent) 82%, rgba(0,0,0,0) 100%);
    opacity: 0.55;
  }
  .compota-de {
    position: absolute; left: 156px; top: 461px;
    font-family: "Montserrat", Arial, sans-serif; font-weight: 500;
    font-size: 13.5px; letter-spacing: 0.6px; color: var(--accent); white-space: nowrap;
  }
  .label--plum .compota-de { left: 148px; top: 476px; }

  .producer, .ingredients {
    position: absolute; top: 531px;
    font-family: "Oswald", "Arial Narrow", sans-serif; font-weight: 300;
    font-size: 7.6px; line-height: 13px; color: var(--accent); white-space: nowrap;
  }
  .producer { left: 21px; }
  .ingredients { left: 184px; }
  .producer strong, .ingredients strong { font-weight: 400; font-size: 9px; }
  .qty { font-size: 11.5px; font-weight: 400; }
  .divider {
    position: absolute; left: 171px; top: 533px; height: 38px;
    border-left: 1.4px dotted var(--accent);
  }

  /* ---------- Nutrition panel for approval ---------- */
  .facts {
    position: absolute; left: 788px; top: 250px; width: 350px; height: 476px;
    border: 2px solid var(--ink); border-radius: 10px; background: var(--paper);
    font-family: "Arimo", Arial, sans-serif; color: var(--ink); overflow: hidden;
  }
  .facts > * { position: absolute; white-space: nowrap; }
  .facts__title { left: 17px; top: 20px; font-size: 30px; line-height: 34px; font-weight: 700; letter-spacing: -0.5px; }
  .facts__serving { left: 22px; top: 59px; font-size: 17px; line-height: 18px; }
  .facts__prepared { left: 22px; top: 82px; font-size: 17px; line-height: 18px; font-style: italic; }
  .facts__bar { left: 22px; width: 306px; height: 8px; background: var(--ink); }
  .facts__bar--top { top: 110px; }
  .facts__bar--bottom { top: 414px; }
  .facts__rule { left: 22px; width: 306px; height: 2px; background: var(--ink); }
  .facts__row { left: 20px; font-size: 24px; line-height: 26px; }
  .facts__row--indent { left: 41px; }
  .facts__row strong { font-weight: 700; }
  .facts__note { left: 20px; top: 432px; font-size: 22px; line-height: 24px; }
</style>
</head>
<body>
<main class="board">

  <p class="note note--additional">ADDITIONAL</p>
  <p class="note note--revised">COLOR REVISED</p>
  <p class="note note--approval">FOR APPROVAL<br>AND WILL BE APLLY<br>ON ALL FLAVORS</p>

  <!-- Pumpkin label -->
  <article class="label label--pumpkin">
    <svg class="label__shape" viewBox="0 0 336 588" width="336" height="588" aria-hidden="true">
      <path fill="#000" d="M120 226 A120 120 0 1 1 216 226 L216 420 L312 420 Q336 420 336 444 L336 588 L0 588 L0 444 Q0 420 24 420 L120 420 Z"/>
    </svg>
    <div class="brand"><span class="brand__dot"></span><span class="brand__name">VALE TINTO</span></div>
    <div class="fruit-art fruit-art--main" role="img" aria-label="Illustration of an orange pumpkin on golden honeycomb outlines"></div>
    <section class="mini-facts">
      <div class="mini-facts__title">NUTRITIONAL VALUE</div>
      <div class="mini-facts__sub">Serving Size: 100g</div>
      <div class="mini-facts__sub"><em>Prepared with 60g fruit per 100g</em></div>
      <div class="mini-facts__bar"></div>
      <div class="mini-facts__row mini-facts__row--plain">Energy 262 kcal</div>
      <div class="mini-facts__row mini-facts__right">1110 kj</div>
      <div class="mini-facts__row">Carbohydrates 64.9</div>
      <div class="mini-facts__row mini-facts__indent">Sugar 64.9</div>
      <div class="mini-facts__row">Lipids 0 g</div>
      <div class="mini-facts__row mini-facts__indent">Saturated 0 g</div>
      <div class="mini-facts__row">Proteins 0.2</div>
      <div class="mini-facts__row mini-facts__row--plain">Salt &lt;0.01</div>
      <div class="mini-facts__bar"></div>
      <div class="mini-facts__note">Bibliographic reference value.</div>
    </section>
    <div class="fruit-art fruit-art--small" role="img" aria-label="Small pumpkin illustration on honeycomb outlines"></div>
    <div class="lettering" role="img" aria-label="Script lettering: Abóbora"></div>
    <p class="compota-de">COMPOTA DE</p>
    <p class="producer">Produzido e embalado por: <strong>VALE TINTO</strong><br>Rua das Amoreiras, 112 V.N. Gaia, PORTUGAL<br>valetinto.doces@mail.pt</p>
    <span class="divider"></span>
    <p class="ingredients"><strong>Ingredientes:</strong> Abóbora (60%),<br>acucar, agua, sumo de limao e pectina.<br><span class="qty">Quant. 220 gr.</span></p>
  </article>

  <!-- Plum label -->
  <article class="label label--plum">
    <svg class="label__shape" viewBox="0 0 336 588" width="336" height="588" aria-hidden="true">
      <path fill="#000" d="M120 226 A120 120 0 1 1 216 226 L216 420 L312 420 Q336 420 336 444 L336 588 L0 588 L0 444 Q0 420 24 420 L120 420 Z"/>
    </svg>
    <div class="brand"><span class="brand__dot"></span><span class="brand__name">VALE TINTO</span></div>
    <div class="fruit-art fruit-art--main" role="img" aria-label="Illustration of whole and halved plums with leaves on white honeycomb outlines"></div>
    <section class="mini-facts">
      <div class="mini-facts__title">NUTRITIONAL VALUE</div>
      <div class="mini-facts__sub">Serving Size: 100g</div>
      <div class="mini-facts__sub"><em>Prepared with 60g fruit per 100g</em></div>
      <div class="mini-facts__bar"></div>
      <div class="mini-facts__row mini-facts__row--plain">Energy 262 kcal</div>
      <div class="mini-facts__row mini-facts__right">1110 kj</div>
      <div class="mini-facts__row">Carbohydrates 64.9</div>
      <div class="mini-facts__row mini-facts__indent">Sugar 64.9</div>
      <div class="mini-facts__row">Lipids 0 g</div>
      <div class="mini-facts__row mini-facts__indent">Saturated 0 g</div>
      <div class="mini-facts__row">Proteins 0.2</div>
      <div class="mini-facts__row mini-facts__row--plain">Salt &lt;0.01</div>
      <div class="mini-facts__bar"></div>
      <div class="mini-facts__note">Bibliographic reference value.</div>
    </section>
    <div class="fruit-art fruit-art--small" role="img" aria-label="Small plum illustration on honeycomb outlines"></div>
    <div class="lettering" role="img" aria-label="Script lettering: Ameixa"></div>
    <p class="compota-de">COMPOTA DE</p>
    <p class="producer">Produzido e embalado por: <strong>VALE TINTO</strong><br>Rua das Amoreiras, 112 V.N. Gaia, PORTUGAL<br>valetinto.doces@mail.pt</p>
    <span class="divider"></span>
    <p class="ingredients"><strong>Ingredientes:</strong> Ameixa (60%),<br>acucar, agua, sumo de limao e pectina.<br><span class="qty">Quant. 220 gr.</span></p>
  </article>

  <!-- Nutrition panel -->
  <section class="facts">
    <h2 class="facts__title">NUTRITIONAL VALUE</h2>
    <p class="facts__serving">Serving Size: 100g</p>
    <p class="facts__prepared">Prepared with 60g fruit per 100g</p>
    <span class="facts__bar facts__bar--top"></span>
    <p class="facts__row" style="top:124px">Energy 262 kcal</p>
    <p class="facts__row" style="top:159px; left:128px">1110 kj</p>
    <span class="facts__rule" style="top:191px"></span>
    <p class="facts__row" style="top:197px"><strong>Carbohydrates</strong> 64.9</p>
    <p class="facts__row facts__row--indent" style="top:231px">Sugar 64.9</p>
    <span class="facts__rule" style="top:261px"></span>
    <p class="facts__row" style="top:267px"><strong>Lipids</strong> 0 g</p>
    <span class="facts__rule" style="top:298px"></span>
    <p class="facts__row facts__row--indent" style="top:302px">Saturated 0 g</p>
    <span class="facts__rule" style="top:333px"></span>
    <p class="facts__row" style="top:337px"><strong>Proteins</strong> 0.2</p>
    <span class="facts__rule" style="top:367px"></span>
    <p class="facts__row" style="top:371px">Salt &lt;0.01</p>
    <span class="facts__bar facts__bar--bottom"></span>
    <p class="facts__note">Bibliographic reference value.</p>
  </section>

</main>
</body>
</html>
```